Granite Surface Works, Inc. Business Card

New business, we do epoxy, polishing concrete, underlayment, fluid applied flooring, sound proofing, double sided, will need 3 sets of cards with 3 different names and phone numbers.
Company: Granite Surface Works, Inc.
Address and Phone: 6339 Charlotte Pike PMB 2183Nashville, TN 37209
(615) 384-7190
www.granitesurfaceworks.example

Target Market(s)

General Contractors, Contractors, Architects

Contact Information for Business Card

1st Card: Derek Halvorsen C. 708.214.8573 e. derek@granitesurfaceworks.example
Vice President
2nd Card: Morgan Brasfield C. 708.361.5847 e. morgan@granitesurfaceworks.example
President
3rd Card: Raj Oti C. 405.617.3328 e. raj@granitesurfaceworks.example
Managing Partner

Font styles to use
Serif
Sans Serif

Requirements
Must have
• Professional Clean Design, Implement colors from Logo or nicely contrasting
Nice to have
• N/A

```html
<!DOCTYPE html>
<html lang="en">
<head>
<meta charset="utf-8">
<title>Granite Surface Works, Inc. – Business Card</title>
<link rel="stylesheet" href="https://fonts.googleapis.com/css2?family=Jost:wght@500;600&family=Montserrat:wght@600;700&display=swap">
<style>
  :root {
    --page: #bdbdbd;
    --card: #f4f4f6;
    --ink: #231f20;
    --blue: #0066b3;
    --green: #6a9f45;
    --blue-soft: #d6e3ef;
    --green-soft: #e3e9df;
  }
  * { margin: 0; padding: 0; box-sizing: border-box; }
  html, body { width: 1200px; height: 382px; overflow: hidden; background: var(--page); }
  .sheet { position: relative; width: 1200px; height: 382px; }
  .card {
    position: absolute; top: 23px; width: 544px; height: 310px;
    background: var(--card); overflow: hidden;
    box-shadow: 1px 2px 4px rgba(0,0,0,0.25);
  }
  .card--front { left: 43px; }
  .card--back { left: 616px; }

  .brand-square { position: absolute; background: var(--blue); }
  .brand-name {
    position: absolute; font-family: "Jost", sans-serif; font-weight: 600;
    color: var(--ink); text-transform: uppercase; line-height: 1;
  }
  .card--front .brand-square { left: 39px; top: 40px; width: 44px; height: 44px; }
  .card--front .brand-name { left: 39px; top: 100px; font-size: 36px; }
  .card--back .brand-square { left: 27px; top: 30px; width: 70px; height: 70px; }
  .card--back .brand-name { left: 110px; top: 31px; font-size: 23px; }

  .decor { position: absolute; top: 0; right: 0; height: 310px; }
  .card--front .decor {
    width: 298px;
    background: linear-gradient(135deg, var(--card) 0%, var(--blue-soft) 45%, var(--green-soft) 100%);
  }
  .card--back .decor {
    width: 268px;
    background: linear-gradient(135deg, var(--card) 0%, var(--blue) 45%, var(--green) 100%);
  }

  .accent-bar { position: absolute; left: 0; top: 166px; width: 4px; height: 34px; background: var(--blue); }
  .person-name {
    position: absolute; left: 24px; top: 164px;
    font-family: "Jost", sans-serif; font-weight: 600; font-size: 21px; line-height: 1;
    color: var(--ink); letter-spacing: 0.2px; white-space: nowrap;
  }
  .person-title {
    position: absolute; left: 26px; top: 191px;
    font-family: "Montserrat", sans-serif; font-weight: 600; font-size: 10px; line-height: 1;
    letter-spacing: 2px; color: var(--green);
  }
  .title-rule {
    position: absolute; left: 28px; top: 207px; width: 186px; height: 1px;
    background: linear-gradient(90deg, #8fb3d6, rgba(143,179,214,0));
  }
  .contact {
    position: absolute; left: 24px; display: flex; align-items: center; gap: 7px;
    font-family: "Montserrat", sans-serif; font-weight: 700; color: var(--ink);
    white-space: nowrap;
  }
  .contact svg { width: 20px; height: 20px; flex: none; }
  .contact--phone { top: 233px; font-size: 12.5px; letter-spacing: 1px; }
  .contact--email { top: 262px; font-size: 10.5px; }
</style>
</head>
<body>
<div class="sheet">
  <section class="card card--front">
    <div class="brand-square"></div>
    <div class="brand-name">Granite<br>Surface<br>Works</div>
    <div class="decor" role="img" aria-label="Large faint brand decoration"></div>
  </section>

  <section class="card card--back">
    <div class="brand-square"></div>
    <div class="brand-name">Granite<br>Surface<br>Works</div>
    <div class="decor" role="img" aria-label="Large brand decoration in blue and green"></div>

    <div class="accent-bar"></div>
    <div class="person-name">DEREK HALVORSEN C.</div>
    <div class="person-title">VICE PRESIDENT</div>
    <div class="title-rule"></div>

    <div class="contact contact--phone">
      <svg viewBox="0 0 20 20" aria-hidden="true">
        <circle cx="10" cy="10" r="9" fill="none" stroke="#6a9f45" stroke-width="1.3"/>
        <path d="M6.3 5.2l1.8-.4 1.2 2.6-1.1.9c.6 1.3 1.6 2.3 2.9 2.9l.9-1.1 2.6 1.2-.4 1.8c-.2.6-.8.9-1.4.8C9.7 13.4 6.6 10.3 5.9 6.6c-.1-.6.2-1.2.4-1.4z" fill="#6a9f45"/>
      </svg>
      <span>708.214.8573</span>
    </div>
    <div class="contact contact--email">
      <svg viewBox="0 0 20 20" aria-hidden="true">
        <circle cx="10" cy="10" r="9" fill="none" stroke="#6a9f45" stroke-width="1.3"/>
        <rect x="5" y="6.5" width="10" height="7" fill="none" stroke="#6a9f45" stroke-width="1"/>
        <path d="M5 6.5l5 4 5-4M5 13.5l3.6-3.2M15 13.5l-3.6-3.2" fill="none" stroke="#6a9f45" stroke-width="1"/>
      </svg>
      <span>derek@granitesurfaceworks.example</span>
    </div>
  </section>
</div>
</body>
</html>
```